Social Media designs (LinkedIn banner, LinkedIn posts, Instagram)

Hello designers!
We are looking to create some more concepts for our social media identity for a search firm (recruitment company)
I have attached a "brand toolkit" that shows our brand, logo, colour scheme to guide you with regards to colours and identiy.

You will see in the brand toolkit there are some examples of;
- A LinkedIn banner for the company (page 23)
- Social Media posts for LinkedIn and Instagram (page 21)

What we are looking for...

We don't really like the current LinkedIn banner ideas. We would like to see more concepts that look more aesthetically pleasing - the current ideas look quite dull.

We DO like the social media post concepts but we would like to have more templates/options that we can use (similar themes)

We welcome submissions for Social Media designs that we can use with our company branding. Thank you for your work in advance!

```html
<!DOCTYPE html>
<html lang="en">
<head>
<meta charset="utf-8">
<title>Harlow Reed – Social Media Set</title>
<link rel="stylesheet" href="https://fonts.googleapis.com/css2?family=Jost:wght@400;500;600&display=swap">
<style>
  :root {
    --green: #4ca584;
    --green-mid: #3f8f72;
    --green-deep: #2a6552;
    --green-dark: #173a30;
    --mint: #8fe6c4;
    --white: #ffffff;
    --canvas: #ffffff;
  }
  * { margin: 0; padding: 0; box-sizing: border-box; }
  html, body {
    width: 1183px; height: 1200px; overflow: hidden;
    background: var(--canvas);
    font-family: "Jost", "Helvetica Neue", Arial, sans-serif;
  }
  .canvas { position: relative; width: 1183px; height: 1200px; }

  /* LinkedIn banners */
  .banner {
    position: absolute; left: 103px; width: 960px; height: 240px; overflow: hidden;
  }
  .banner--first { top: 62px; }
  .banner--second { top: 352px; }
  .banner__photo { position: absolute; inset: 0; }
  .banner--first .banner__photo {
    background:
      linear-gradient(90deg, rgba(76,165,132,.85) 0%, rgba(76,165,132,.55) 12%, rgba(23,58,48,.75) 40%, rgba(23,58,48,.9) 55%, rgba(76,165,132,.75) 70%, rgba(76,165,132,.5) 100%),
      linear-gradient(180deg, #8a9690 0%, #5f6b66 60%, #3e4844 100%);
  }
  .banner--second .banner__photo {
    background:
      linear-gradient(90deg, rgba(23,58,48,.92) 0%, rgba(42,101,82,.7) 25%, rgba(76,165,132,.85) 45%, rgba(76,165,132,.6) 65%, rgba(23,58,48,.9) 100%),
      linear-gradient(180deg, #8a9690 0%, #5f6b66 60%, #3e4844 100%);
  }
  .banner__panel {
    position: absolute; top: 0; bottom: 0; left: 542px; right: 0;
    background: linear-gradient(90deg, rgba(76,165,132,.35), rgba(76,165,132,0));
  }
  .banner__title {
    position: absolute; left: 354px; top: 92px;
    font-size: 46px; line-height: 56px; font-weight: 500; letter-spacing: .3px;
    white-space: nowrap;
    -webkit-background-clip: text; background-clip: text; color: transparent;
  }
  .banner--first .banner__title {
    background-image: linear-gradient(90deg, #6b9c88 0%, #7fd6b2 40%, #a4f3d3 100%);
  }
  .banner--second .banner__title {
    background-image: linear-gradient(90deg, #a4f3d3 0%, #8fe6c4 60%, #5f9a84 100%);
  }

  /* Square posts */
  .post {
    position: absolute; top: 660px; width: 446px; height: 446px; overflow: hidden;
    background: linear-gradient(160deg, var(--green-deep) 0%, var(--green-mid) 45%, var(--green) 100%);
  }
  .post--track { left: 102px; }
  .post--story { left: 610px; }
  .post__photo { position: absolute; left: 0; top: 0; width: 446px; height: 446px; }

  .post__headline { position: absolute; color: var(--white); font-weight: 500; }
  .post--track .post__headline {
    left: 31px; top: 32px; font-size: 40px; line-height: 37px;
  }
  .post--story .post__headline {
    left: 31px; top: 36px; font-size: 22px; line-height: 23px; letter-spacing: .2px;
  }
  .post__body {
    position: absolute; left: 36px; top: 208px; width: 145px;
    color: var(--white); font-size: 10px; line-height: 12px;
  }
  .post__tagline {
    position: absolute; left: 31px; top: 140px;
    color: var(--white); font-size: 10px; font-weight: 500;
  }
  .brand {
    position: absolute; left: 35px; top: 372px;
    display: flex; align-items: center; gap: 12px;
  }
  .brand__square { width: 34px; height: 34px; background: var(--white); }
  .brand__name { color: var(--white); font-size: 19px; line-height: 19px; font-weight: 400; }
</style>
</head>
<body>
<main class="canvas">

  <section class="banner banner--first">
    <div class="banner__photo" role="img" aria-label="City street of tall stone apartment buildings with a hotel sign, tinted green"></div>
    <div class="banner__panel"></div>
    <h2 class="banner__title">Talent knows no borders</h2>
  </section>

  <section class="banner banner--second">
    <div class="banner__photo" role="img" aria-label="City street of tall stone apartment buildings with a hotel sign, tinted green"></div>
    <h2 class="banner__title">Talent knows no borders</h2>
  </section>

  <article class="post post--track">
    <svg class="post__photo" viewBox="0 0 446 446" role="img" aria-label="Elevated commuter train curving past glass office towers at dusk">
      <defs>
        <linearGradient id="track-photo" x1="0" y1="0" x2="0" y2="1">
          <stop offset="0" stop-color="#e9ddd3"/>
          <stop offset="0.35" stop-color="#7d7a78"/>
          <stop offset="0.7" stop-color="#4a3c36"/>
          <stop offset="1" stop-color="#2a2624"/>
        </linearGradient>
      </defs>
      <path d="M279 0 H446 V446 H142 L200 400 L279 330 Z" fill="url(#track-photo)"/>
    </svg>
    <h1 class="post__headline">Stay on<br>the right<br>career<br>track</h1>
    <p class="post__body">We go beyond finding candidates the right job - we provide tailored guidance and support to ensure long-term career success.</p>
    <div class="brand">
      <span class="brand__square"></span>
      <span class="brand__name">Harlow<br>Reed</span>
    </div>
  </article>

  <article class="post post--story">
    <svg class="post__photo" viewBox="0 0 446 446" role="img" aria-label="Photo of a smiling professional woman with long red hair in a black top, standing in a bright office">
      <defs>
        <linearGradient id="story-photo" x1="0" y1="0" x2="1" y2="1">
          <stop offset="0" stop-color="#d9c0b0"/>
          <stop offset="0.5" stop-color="#8a6a5c"/>
          <stop offset="1" stop-color="#2a2628"/>
        </linearGradient>
      </defs>
      <path d="M299 0 H446 V446 H190 L175 170 L299 150 Z" fill="url(#story-photo)"/>
    </svg>
    <h1 class="post__headline">Building a career<br>you love is the<br>ultimate success<br>story</h1>
    <p class="post__tagline">- let's write yours!</p>
    <div class="brand">
      <span class="brand__square"></span>
      <span class="brand__name">Harlow<br>Reed</span>
    </div>
  </article>

</main>
</body>
</html>
```